Updating our Raw Materials Brochure

Please update and modify (to add more space for the additional text) the brochure designed for us in January (see attached file) so we can circulate a May 2021 version. Thanks and hope your family is OK despite the terrible tragedy going on with Covid-19 in India. Best wishes!

```html
<!DOCTYPE html>
<html lang="en">
<head>
<meta charset="utf-8">
<title>Raw Materials May 2021 Market Update</title>
<link href="https://fonts.googleapis.com/css2?family=Montserrat:wght@600;700;800&family=Open+Sans:wght@400;600&display=swap" rel="stylesheet">
<style>
  :root{
    --ink:#1b1b1d;
    --ink-soft:#2c2c30;
    --red:#d7262e;
    --white:#ffffff;
    --text:#3a3a3a;
    --muted:#8a8a8a;
    --grid:#e6e6e6;
    --blue:#3d7cc9;
    --backdrop:#eef0f1;
  }
  *{box-sizing:border-box;margin:0;padding:0}
  html,body{width:863px;height:1200px;overflow:hidden;background:var(--backdrop)}
  body{font-family:"Open Sans",Arial,sans-serif;color:var(--text);position:relative}

  .page{position:absolute;top:309px;width:411px;height:582px;background:var(--white);overflow:hidden;box-shadow:0 2px 10px rgba(0,0,0,.12)}
  .page--front{left:14px}
  .page--back{left:438px}

  .brand{display:flex;align-items:center;gap:6px}
  .brand-mark{width:10px;height:10px;background:var(--red)}
  .brand-name{font-family:"Montserrat",Arial,sans-serif;font-weight:700;font-size:8px;letter-spacing:.6px;color:var(--white);text-transform:uppercase}

  /* front header */
  .cover{position:absolute;left:0;top:0;width:411px;height:200px;background:var(--ink);overflow:hidden;border-bottom:3px solid var(--red)}
  .cover .brand{position:absolute;left:22px;top:20px}
  .hero-photo{position:absolute;left:228px;top:-62px;width:230px;height:230px;border-radius:50%;
    background:radial-gradient(circle at 40% 55%,#c9d3dc 0%,#7f8d99 30%,#3c4651 65%,#1e242b 100%);
    border:5px solid var(--red);box-shadow:0 0 0 4px var(--ink-soft)}
  .cover-title{position:absolute;left:22px;top:104px;font-family:"Montserrat",Arial,sans-serif;font-weight:800;font-size:21px;line-height:1.1;color:var(--white);text-transform:uppercase}
  .accent{color:var(--red)}

  /* back header */
  .masthead{position:absolute;left:0;top:0;width:411px;height:96px;background:var(--ink);border-bottom:3px solid var(--red);text-align:center}
  .masthead .brand{justify-content:center;margin-top:14px}
  .masthead-title{font-family:"Montserrat",Arial,sans-serif;font-weight:800;font-size:17px;line-height:1.15;color:var(--white);text-transform:uppercase;margin-top:12px}

  .columns{position:absolute;left:22px;width:367px;display:grid;grid-template-columns:1fr 1fr;column-gap:15px}
  .page--front .columns{top:216px}
  .page--back .columns{top:110px}

  .section-title{font-family:"Montserrat",Arial,sans-serif;font-weight:800;font-size:10.5px;line-height:1.15;text-transform:uppercase;color:var(--ink);padding-left:6px;border-left:2px solid var(--red);margin-bottom:7px}
  p{font-size:6.3px;line-height:1.55;margin-bottom:5px}
  p.lead{font-weight:600;color:var(--ink)}

  .chart{margin:3px 0 7px}
  .chart-caption{font-size:5.5px;color:var(--muted);text-align:center;font-weight:600;margin-bottom:2px}
  .chart svg{display:block}

  .footer{position:absolute;left:0;bottom:0;width:411px;height:44px;background:var(--ink);border-top:3px solid var(--red);display:flex;align-items:center;padding:0 22px;gap:12px}
  .call-tag{background:var(--red);color:var(--white);font-family:"Montserrat",Arial,sans-serif;font-weight:700;font-size:6.5px;padding:4px 7px;text-transform:uppercase;letter-spacing:.6px}
  .contact{display:flex;align-items:center;gap:4px;color:var(--white);font-family:"Montserrat",Arial,sans-serif;font-weight:700;font-size:8px}
  .contact svg{flex:none}
  .web{margin-left:auto}
</style>
</head>
<body>

  <!-- FRONT PAGE -->
  <article class="page page--front">
    <header class="cover">
      <div class="brand"><span class="brand-mark"></span><span class="brand-name">Corvane Industries</span></div>
      <div class="hero-photo" role="img" aria-label="Photograph of an industrial plant interior with steel pipework"></div>
      <h1 class="cover-title">Raw Materials<br><span class="accent">May 2021</span><br>Market Update</h1>
    </header>

    <main class="columns">
      <section>
        <h2 class="section-title">Global <span class="accent">Shortage</span></h2>
        <p class="lead">Supply of key raw materials stayed tight through the spring, as demand recovered faster than producers could restart idled capacity.</p>
        <p>Resin, steel and specialty chemical markets all reported extended lead times. Many suppliers placed customers on allocation while spot prices climbed to multi-year highs.</p>
        <p>Freight disruption added pressure. Container rates on major routes stayed far above pre-pandemic levels, and port congestion delayed shipments by weeks.</p>
        <p>Weather events early in the year removed a large share of petrochemical output, and several plants are still completing repairs before returning to full rates.</p>
        <p>We expect conditions to ease gradually in the second half, but buyers should plan for continued volatility and secure supply commitments early.</p>
      </section>

      <section>
        <h2 class="section-title">Key <span class="accent">Constraints</span></h2>
        <p>Several factors continue to restrict availability and keep prices elevated across most categories we track.</p>
        <figure class="chart">
          <figcaption class="chart-caption">Monthly price index, Jan 2020 – May 2021</figcaption>
          <svg width="176" height="84" viewBox="0 0 176 84" aria-label="Line chart of rising monthly price index">
            <g stroke="#e6e6e6" stroke-width=".6"><line x1="14" y1="10" x2="174" y2="10"/><line x1="14" y1="28" x2="174" y2="28"/><line x1="14" y1="46" x2="174" y2="46"/><line x1="14" y1="64" x2="174" y2="64"/></g>
            <line x1="14" y1="74" x2="174" y2="74" stroke="#999" stroke-width=".6"/>
            <line x1="14" y1="6" x2="14" y2="74" stroke="#999" stroke-width=".6"/>
            <g font-family="Open Sans, sans-serif" font-size="4.5" fill="#8a8a8a" text-anchor="end"><text x="12" y="12">200</text><text x="12" y="30">150</text><text x="12" y="48">100</text><text x="12" y="66">50</text></g>
            <g font-family="Open Sans, sans-serif" font-size="4.5" fill="#8a8a8a" text-anchor="middle"><text x="19" y="81">J</text><text x="50" y="81">A</text><text x="81" y="81">J</text><text x="112" y="81">O</text><text x="143" y="81">J</text><text x="170" y="81">M</text></g>
            <polyline fill="none" stroke="#9a9a9a" stroke-width="1" points="19,52 29,53 39,56 50,58 60,56 70,55 81,54 91,53 101,52 112,50 122,49 132,48 143,46 153,45 163,44 170,43"/>
            <polyline fill="none" stroke="#d7262e" stroke-width="1.3" points="19,55 29,56 39,60 50,62 60,59 70,57 81,55 91,52 101,49 112,46 122,42 132,37 143,30 153,22 163,15 170,11"/>
          </svg>
        </figure>
        <p>Labour shortages at production sites and logistics hubs have slowed output, while postponed maintenance is stacking downtime into the coming quarters.</p>
        <p>Inventories across the supply chain sit at historically low levels, leaving little buffer against new disruptions.</p>
        <p>Our team is monitoring each market closely and will share updates as the situation develops.</p>
      </section>
    </main>

    <footer class="footer">
      <span class="call-tag">Call us at</span>
      <span class="contact">
        <svg width="8" height="8" viewBox="0 0 24 24" aria-hidden="true"><path fill="#d7262e" d="M6.6 10.8a15.1 15.1 0 0 0 6.6 6.6l2.2-2.2a1 1 0 0 1 1-.25 11.4 11.4 0 0 0 3.6.57 1 1 0 0 1 1 1V20a1 1 0 0 1-1 1A17 17 0 0 1 3 4a1 1 0 0 1 1-1h3.5a1 1 0 0 1 1 1c0 1.25.2 2.45.57 3.6a1 1 0 0 1-.25 1z"/></svg>
        800 555 0142 (4582)
      </span>
      <span class="contact web">
        <svg width="8" height="8" viewBox="0 0 24 24" aria-hidden="true"><circle cx="12" cy="12" r="9" fill="none" stroke="#d7262e" stroke-width="2.4"/><path d="M3 12h18M12 3c3 3 3 15 0 18M12 3c-3 3-3 15 0 18" fill="none" stroke="#d7262e" stroke-width="2"/></svg>
        www.corvane-ind.com
      </span>
    </footer>
  </article>

  <!-- BACK PAGE -->
  <article class="page page--back">
    <header class="masthead">
      <div class="brand"><span class="brand-mark"></span><span class="brand-name">Corvane Industries</span></div>
      <h1 class="masthead-title">Raw Materials May 2021<br><span class="accent">Market Update</span></h1>
    </header>

    <main class="columns">
      <section>
        <h2 class="section-title">Logistics limitations<br><span class="accent">vs. demand growth</span></h2>
        <p>Shipping capacity has not kept pace with the rebound in orders. Vessel schedules remain unreliable and equipment is scarce at key export ports.</p>
        <p>Trucking and rail networks are also stretched, adding cost and delay to the final leg of many deliveries.</p>
        <figure class="chart">
          <figcaption class="chart-caption">Freight rate index vs. order volume</figcaption>
          <svg width="176" height="70" viewBox="0 0 176 70" aria-label="Line chart comparing freight rates and order volume">
            <g stroke="#e6e6e6" stroke-width=".6"><line x1="6" y1="10" x2="174" y2="10"/><line x1="6" y1="26" x2="174" y2="26"/><line x1="6" y1="42" x2="174" y2="42"/></g>
            <line x1="6" y1="58" x2="174" y2="58" stroke="#999" stroke-width=".6"/>
            <polyline fill="none" stroke="#3d7cc9" stroke-width="1.1" points="8,40 20,36 32,44 44,38 56,30 68,34 80,26 92,30 104,22 116,28 128,20 140,26 152,18 164,24 172,20"/>
            <polyline fill="none" stroke="#9a9a9a" stroke-width="1" points="8,46 20,44 32,48 44,45 56,42 68,44 80,40 92,41 104,38 116,40 128,36 140,38 152,34 164,36 172,33"/>
          </svg>
        </figure>
        <p>Order growth is expected to stay firm into the third quarter, keeping logistics costs high.</p>
        <figure class="chart">
          <figcaption class="chart-caption">Monthly shipments, thousand tonnes</figcaption>
          <svg width="176" height="64" viewBox="0 0 176 64" aria-label="Bar chart of monthly shipments">
            <line x1="4" y1="58" x2="174" y2="58" stroke="#999" stroke-width=".6"/>
            <g fill="#3d7cc9">
              <rect x="6" y="34" width="5" height="24"/><rect x="14" y="30" width="5" height="28"/><rect x="22" y="36" width="5" height="22"/><rect x="30" y="28" width="5" height="30"/><rect x="38" y="26" width="5" height="32"/><rect x="46" y="30" width="5" height="28"/><rect x="54" y="24" width="5" height="34"/><rect x="62" y="22" width="5" height="36"/><rect x="70" y="26" width="5" height="32"/><rect x="78" y="20" width="5" height="38"/><rect x="86" y="18" width="5" height="40"/><rect x="94" y="22" width="5" height="36"/><rect x="102" y="16" width="5" height="42"/><rect x="110" y="14" width="5" height="44"/><rect x="118" y="18" width="5" height="40"/><rect x="126" y="12" width="5" height="46"/><rect x="134" y="10" width="5" height="48"/><rect x="142" y="14" width="5" height="44"/><rect x="150" y="8" width="5" height="50"/><rect x="158" y="6" width="5" height="52"/><rect x="166" y="9" width="5" height="49"/>
            </g>
          </svg>
        </figure>
      </section>

      <section>
        <figure class="chart">
          <figcaption class="chart-caption">Resin spot price, USD per tonne</figcaption>
          <svg width="176" height="84" viewBox="0 0 176 84" aria-label="Line chart of sharply rising resin spot price">
            <g stroke="#e6e6e6" stroke-width=".6"><line x1="6" y1="10" x2="174" y2="10"/><line x1="6" y1="28" x2="174" y2="28"/><line x1="6" y1="46" x2="174" y2="46"/><line x1="6" y1="64" x2="174" y2="64"/></g>
            <line x1="6" y1="76" x2="174" y2="76" stroke="#999" stroke-width=".6"/>
            <polyline fill="none" stroke="#9a9a9a" stroke-width="1" points="8,66 30,65 52,66 74,64 96,63 118,62 140,60 172,58"/>
            <polyline fill="none" stroke="#d7262e" stroke-width="1.3" points="8,70 30,69 52,70 74,68 96,66 118,62 132,54 144,42 156,26 166,14 172,9"/>
          </svg>
        </figure>
        <p>Resin prices accelerated sharply from January as outages met a rapid recovery in packaging and construction demand.</p>
        <h2 class="section-title" style="margin-top:8px">Polyethylene and<br>polyurethane <span class="accent">prices<br>near record highs</span></h2>
        <p>Polyethylene contracts settled at their highest levels in over a decade, with further increases nominated for June by several producers.</p>
        <p>Polyurethane feedstocks remain constrained, and converters report difficulty sourcing volumes beyond committed contracts.</p>
        <figure class="chart">
          <figcaption class="chart-caption">Contract price change by month, %</figcaption>
          <svg width="176" height="64" viewBox="0 0 176 64" aria-label="Bar chart of monthly contract price changes">
            <line x1="4" y1="58" x2="174" y2="58" stroke="#999" stroke-width=".6"/>
            <g fill="#3d7cc9">
              <rect x="6" y="46" width="5" height="12"/><rect x="14" y="44" width="5" height="14"/><rect x="22" y="48" width="5" height="10"/><rect x="30" y="42" width="5" height="16"/><rect x="38" y="40" width="5" height="18"/><rect x="46" y="38" width="5" height="20"/><rect x="54" y="40" width="5" height="18"/><rect x="62" y="34" width="5" height="24"/><rect x="70" y="32" width="5" height="26"/><rect x="78" y="30" width="5" height="28"/><rect x="86" y="28" width="5" height="30"/><rect x="94" y="30" width="5" height="28"/><rect x="102" y="24" width="5" height="34"/><rect x="110" y="22" width="5" height="36"/><rect x="118" y="18" width="5" height="40"/><rect x="126" y="20" width="5" height="38"/><rect x="134" y="14" width="5" height="44"/><rect x="142" y="12" width="5" height="46"/><rect x="150" y="10" width="5" height="48"/><rect x="158" y="7" width="5" height="51"/><rect x="166" y="5" width="5" height="53"/>
            </g>
          </svg>
        </figure>
      </section>
    </main>

    <footer class="footer">
      <span class="call-tag">Call us at</span>
      <span class="contact">
        <svg width="8" height="8" viewBox="0 0 24 24" aria-hidden="true"><path fill="#d7262e" d="M6.6 10.8a15.1 15.1 0 0 0 6.6 6.6l2.2-2.2a1 1 0 0 1 1-.25 11.4 11.4 0 0 0 3.6.57 1 1 0 0 1 1 1V20a1 1 0 0 1-1 1A17 17 0 0 1 3 4a1 1 0 0 1 1-1h3.5a1 1 0 0 1 1 1c0 1.25.2 2.45.57 3.6a1 1 0 0 1-.25 1z"/></svg>
        800 555 0142 (4582)
      </span>
      <span class="contact web">
        <svg width="8" height="8" viewBox="0 0 24 24" aria-hidden="true"><circle cx="12" cy="12" r="9" fill="none" stroke="#d7262e" stroke-width="2.4"/><path d="M3 12h18M12 3c3 3 3 15 0 18M12 3c-3 3-3 15 0 18" fill="none" stroke="#d7262e" stroke-width="2"/></svg>
        www.corvane-ind.com
      </span>
    </footer>
  </article>

</body>
</html>
```